Tamarack Hearth Partners Business Card

Looking for a new business card layout. We are a real estate firm w/ a logo, old design attached. Must keep the same elements on there, just need a fresh look and possible some foil accents. Looking for a simpler design w/ more modern style.

Target Market(s)

Real Estate clients

Industry/Entity Type

Real Estate Agent

Contact Information for Business Card

see attached

Font styles to use
Sans Serif

Requirements
Must have
• all elements on current biz card
Nice to have
• modern look, simpler than we have!
Should not have
• no serif fonts

```html
<!DOCTYPE html>
<html lang="en">
<head>
<meta charset="utf-8">
<title>Tamarack Hearth Partners – Business Card</title>
<link href="https://fonts.googleapis.com/css2?family=Work+Sans:wght@400;500;700&display=swap" rel="stylesheet">
<style>
  :root {
    --stage: #1a1a1a;
    --card: #262626;
    --card-edge: #2d2d2d;
    --accent-blue: #29a8e0;
    --foil-gold: #c9a04a;
    --text-light: #f2f2f2;
    --photo-light: #d9d2c8;
    --photo-mid: #c79f73;
    --photo-deep: #3cc4c0;
  }
  * { box-sizing: border-box; margin: 0; padding: 0; }
  html, body { width: 1200px; height: 900px; overflow: hidden; }
  body {
    background: var(--stage);
    font-family: "Work Sans", Arial, sans-serif;
    color: var(--text-light);
    position: relative;
  }
  .card {
    position: absolute;
    left: 250px;
    width: 700px;
    height: 400px;
    background: linear-gradient(135deg, var(--card) 0%, var(--card-edge) 100%);
    border-bottom: 6px solid var(--accent-blue);
    overflow: hidden;
    box-shadow: 0 10px 30px rgba(0,0,0,0.5);
  }
  .card--front { top: 40px; }
  .card--back { top: 470px; }

  /* Front */
  .portrait {
    position: absolute;
    left: 0; top: 0;
    width: 300px; height: 100%;
    background: linear-gradient(160deg, var(--photo-light) 0%, var(--photo-mid) 55%, var(--photo-deep) 100%);
  }
  .front-brand {
    position: absolute;
    left: 340px; right: 30px; top: 0; bottom: 0;
    display: flex; align-items: center; justify-content: center;
    text-align: center;
  }
  .foil-name {
    color: var(--foil-gold);
    font-weight: 700;
    font-size: 34px;
    line-height: 1.15;
    letter-spacing: 1px;
    text-transform: uppercase;
  }

  /* Back */
  .back-brand {
    position: absolute;
    left: 40px; top: 0; bottom: 0; width: 270px;
    display: flex; align-items: center; gap: 14px;
  }
  .brand-square {
    width: 18px; height: 18px; flex: none;
    background: var(--accent-blue);
  }
  .brand-name {
    color: var(--text-light);
    font-weight: 700;
    font-size: 30px;
    line-height: 1.1;
    text-transform: uppercase;
  }
  .divider {
    position: absolute;
    left: 330px; top: 60px;
    width: 2px; height: 280px;
    background: var(--accent-blue);
  }
  .contact {
    position: absolute;
    left: 360px; top: 62px; right: 20px;
  }
  .contact__name {
    color: var(--accent-blue);
    font-weight: 500;
    font-size: 38px;
    line-height: 1.05;
  }
  .contact__title {
    font-size: 17px;
    letter-spacing: 1px;
    margin-bottom: 16px;
  }
  .contact__address {
    font-size: 17px;
    letter-spacing: 1px;
    line-height: 1.4;
    margin-bottom: 14px;
  }
  .contact__list { list-style: none; }
  .contact__list li {
    display: flex; align-items: center; gap: 10px;
    font-size: 17px;
    letter-spacing: 1px;
    line-height: 1.55;
  }
  .contact__list svg { width: 13px; height: 13px; flex: none; }
</style>
</head>
<body>
  <section class="card card--front">
    <div class="portrait" role="img" aria-label="Portrait photograph of the principal broker"></div>
    <div class="front-brand">
      <p class="foil-name">Tamarack Hearth<br>Partners</p>
    </div>
  </section>

  <section class="card card--back">
    <div class="back-brand">
      <span class="brand-square"></span>
      <p class="brand-name">Tamarack Hearth Partners</p>
    </div>
    <div class="divider"></div>
    <div class="contact">
      <h1 class="contact__name">Wren Halvorsen</h1>
      <p class="contact__title">Principal Broker</p>
      <p class="contact__address">210 NE Alder Ln<br>Sisters, OR 97759</p>
      <ul class="contact__list">
        <li>
          <svg viewBox="0 0 16 16" fill="none" stroke="var(--accent-blue)" stroke-width="1.6"><path d="M3 1.5h3l1.2 3.5-1.8 1.2a8 8 0 0 0 4.4 4.4l1.2-1.8 3.5 1.2v3a1.5 1.5 0 0 1-1.6 1.5A13 13 0 0 1 1.5 3.1 1.5 1.5 0 0 1 3 1.5z"/></svg>
          541.555.0148
        </li>
        <li>
          <svg viewBox="0 0 16 16" fill="none" stroke="var(--accent-blue)" stroke-width="1.6"><rect x="4" y="1" width="8" height="14" rx="1.5"/><line x1="7" y1="12.5" x2="9" y2="12.5"/></svg>
          541.555.0193
        </li>
        <li>
          <svg viewBox="0 0 16 16" fill="none" stroke="var(--accent-blue)" stroke-width="1.6"><rect x="1" y="3" width="14" height="10" rx="1"/><path d="M1 4l7 5 7-5"/></svg>
          wren@tamarackhearth.com
        </li>
        <li>
          <svg viewBox="0 0 16 16" fill="none" stroke="var(--accent-blue)" stroke-width="1.4"><circle cx="8" cy="8" r="6.5"/><ellipse cx="8" cy="8" rx="3" ry="6.5"/><line x1="1.5" y1="8" x2="14.5" y2="8"/></svg>
          TamarackHearth-Homes.com
        </li>
      </ul>
    </div>
  </section>
</body>
</html>
```